Bright Oak Fitness Facility Business Cards

Business Card Design that incorporates the logo and tagline

Target Market(s)

Fitness, People Who Exercise

Contact Information for Business Card

2817 Mossgrove Bend Road
Alderbrook, Ohio 43190
Phone: 614-555-Jump (5867)
www.brightoakfitness.example
info@brightoakfitness.example

Requirements
Must have
• Logo, Address, Website, email and tagline "Stronger Every Day". Colors should be red/black/grey/white

```html
<!DOCTYPE html>
<html lang="en">
<head>
<meta charset="utf-8">
<title>Bright Oak Fitness – Business Cards</title>
<link rel="stylesheet" href="https://fonts.googleapis.com/css2?family=Bebas+Neue&family=Lato:wght@400&family=Montserrat:wght@600&family=Open+Sans:ital,wght@1,600&display=swap">
<style>
  :root {
    --backdrop: #8f9dd6;
    --paper: #ffffff;
    --ink: #1a1a1a;
    --brand-red: #e3232b;
    --accent-yellow: #e4e02c;
    --card-dark: #1c2b36;
    --tagline-ink: #0d1115;
  }
  * { margin: 0; padding: 0; box-sizing: border-box; }
  html, body { width: 1200px; height: 1200px; overflow: hidden; }
  body { background: var(--backdrop); position: relative; font-family: "Lato", sans-serif; }

  .card { position: absolute; left: 223px; width: 815px; height: 465px; }
  .card-front { top: 76px; background: var(--paper); }
  .card-back { top: 658px; background: var(--card-dark); }

  .identity { position: absolute; right: 449px; top: 205px; text-align: right; }
  .identity-name {
    font-family: "Bebas Neue", sans-serif; color: var(--brand-red);
    font-size: 50px; line-height: 1; letter-spacing: 0.5px;
  }
  .identity-role { font-size: 19px; color: var(--ink); line-height: 1; margin-top: 2px; }

  .divider { position: absolute; left: 406px; top: 208px; width: 3px; height: 66px; background: var(--accent-yellow); }

  .contact-list { position: absolute; left: 437px; top: 203px; list-style: none; }
  .contact-item {
    display: flex; align-items: center; gap: 9px;
    font-size: 19.5px; color: var(--ink); height: 25px;
  }
  .contact-icon { width: 16px; height: 16px; flex: none; }

  .address {
    position: absolute; left: 0; right: 0; top: 410px; text-align: center;
    font-size: 17px; color: var(--ink); letter-spacing: -0.3px;
  }

  .brand-mark {
    position: absolute; left: 0; right: 0; top: 232px;
    display: flex; justify-content: center; align-items: center; gap: 14px;
  }
  .brand-square { width: 26px; height: 26px; background: var(--brand-red); }
  .brand-name {
    font-family: "Montserrat", sans-serif; font-weight: 600;
    font-size: 46px; color: var(--brand-red); letter-spacing: -0.5px;
  }

  .tagline-band { position: absolute; left: 0; right: 0; top: 421px; height: 16px; }
  .band-segment { position: absolute; top: 0; height: 16px; background: var(--brand-red); }
  .band-left { left: 0; width: 298px; }
  .band-right { right: 0; width: 297px; }
  .tagline {
    position: absolute; left: 0; right: 0; top: -6px; text-align: center;
    font-family: "Open Sans", sans-serif; font-style: italic; font-weight: 600;
    font-size: 22px; line-height: 28px; color: var(--tagline-ink);
  }
</style>
</head>
<body>
  <section class="card card-front">
    <div class="identity">
      <div class="identity-name">MARCUS REYES</div>
      <div class="identity-role">MANAGER</div>
    </div>
    <div class="divider"></div>
    <ul class="contact-list">
      <li class="contact-item">
        <svg class="contact-icon" viewBox="0 0 16 16" fill="none" stroke="var(--brand-red)" stroke-width="1.6" aria-hidden="true">
          <path d="M3 2.5l2.5-.5 1.3 3-1.6 1.2a8 8 0 0 0 4.6 4.6l1.2-1.6 3 1.3-.5 2.5C8 13.5 2.5 8 3 2.5z"/>
          <path d="M9.5 3a4 4 0 0 1 3.5 3.5M9.5 1a6 6 0 0 1 5.5 5.5"/>
        </svg>
        <span>614-555-Jump (5867)</span>
      </li>
      <li class="contact-item">
        <svg class="contact-icon" viewBox="0 0 16 16" fill="none" stroke="var(--brand-red)" stroke-width="1.3" aria-hidden="true">
          <rect x="1" y="3" width="14" height="10"/>
          <path d="M1 3l7 6 7-6M1 13l5-5M15 13l-5-5"/>
        </svg>
        <span>info@brightoakfitness.example</span>
      </li>
      <li class="contact-item">
        <svg class="contact-icon" viewBox="0 0 16 16" fill="none" stroke="var(--brand-red)" stroke-width="1.3" aria-hidden="true">
          <circle cx="8" cy="8" r="6.5"/>
          <ellipse cx="8" cy="8" rx="3" ry="6.5"/>
          <path d="M1.5 8h13M2.5 4.8h11M2.5 11.2h11"/>
        </svg>
        <span>www.brightoakfitness.example</span>
      </li>
    </ul>
    <p class="address">2817 Mossgrove Bend Road&nbsp; Alderbrook, Ohio 43190</p>
  </section>

  <section class="card card-back">
    <div class="brand-mark">
      <span class="brand-square"></span>
      <span class="brand-name">BRIGHT OAK FITNESS</span>
    </div>
    <div class="tagline-band">
      <span class="band-segment band-left"></span>
      <span class="band-segment band-right"></span>
      <p class="tagline">Stronger Every Day</p>
    </div>
  </section>
</body>
</html>
```